Kestrelwood Restaurnt Lunch Menu Redesign:

We have two lunch special menus that need to be reformatted into a 4.25inx11in and need a graphics design update. Some menu items need to change and some descriptions need to updated. This new menu should double sided with the Main Dining Lunch Menu on the front side and Teppanyaki Lunch menu on the back.

Both menus should follow the same design formatting as the main dining lunch menu (font, sizing, ect.)

```html
<!DOCTYPE html>
<html lang="en">
<head>
<meta charset="utf-8">
<title>Kestrelwood Restaurnt – Lunch Menus</title>
<link href="https://fonts.googleapis.com/css2?family=Cinzel+Decorative:wght@700&family=Cormorant+Garamond:ital,wght@1,500;1,600&family=Roboto:ital,wght@0,400;0,500;1,400&display=swap" rel="stylesheet">
<style>
:root{
  --backdrop:#5b5b5b;
  --paper:#f8f4dc;
  --gold:#b8891f;
  --ink:#1e1e1e;
  --muted:#6a6150;
}
*{box-sizing:border-box;margin:0;padding:0}
html,body{width:1200px;height:666px;overflow:hidden}
body{background:var(--backdrop);display:flex;justify-content:center;align-items:center;gap:40px;font-family:'Roboto',sans-serif;color:var(--ink)}
.menu-card{position:relative;width:240px;height:622px;background:var(--paper);padding:9px;overflow:hidden}
.menu-frame{position:relative;height:100%;border:1.5px solid var(--gold);outline:0.6px solid var(--gold);outline-offset:-3.5px;padding:10px 10px 8px}
.menu-title{font-family:'Cinzel Decorative',serif;color:var(--gold);font-size:17.5px;text-align:center;line-height:1;letter-spacing:.2px}
.menu-hours{font-family:'Cormorant Garamond',serif;font-style:italic;color:var(--gold);font-size:10.5px;text-align:center;margin-top:2px}
.divider{display:flex;align-items:center;justify-content:center;margin:6px 12px 5px;height:6px}
.divider::before,.divider::after{content:"";flex:1;height:0.6px;background:var(--gold)}
.divider span{width:26px;height:6px;background:
  linear-gradient(45deg,transparent 35%,var(--gold) 35% 65%,transparent 65%) center/6px 6px no-repeat}
.divider span{position:relative}
.divider span::before,.divider span::after{content:"";position:absolute;top:1.5px;width:3px;height:3px;background:var(--gold);transform:rotate(45deg)}
.divider span::before{left:3px}.divider span::after{right:3px}
.section-title{font-family:'Cinzel Decorative',serif;color:var(--gold);font-size:11.5px;text-align:center;line-height:1.1}
.section-note{font-family:'Cormorant Garamond',serif;font-style:italic;font-size:7.6px;text-align:center;line-height:1.2;margin-top:2px;color:var(--ink)}
.section-note.gold{color:var(--gold);font-size:10px;line-height:1.15;margin-bottom:6px}
.item-list{list-style:none;margin-top:5px}
.item{display:flex;justify-content:space-between;align-items:flex-start;font-size:7.4px;line-height:1.25}
.item .price{font-weight:500;font-size:8.6px}
.item-desc{display:block;font-style:italic;color:var(--muted);font-size:6.2px}
.sandwiches .item{margin-bottom:3px}
.inline-desc{font-style:italic;color:var(--muted);font-size:6.2px}
.sushi-grid{display:grid;grid-template-columns:1fr 1fr;column-gap:4px;list-style:none;margin-top:5px;padding:0 2px}
.sushi-grid li{font-size:7.2px;line-height:1.68;white-space:nowrap}
.sushi-grid li::before{content:"";display:inline-block;width:5px;height:5px;background:var(--gold);transform:rotate(45deg);margin-right:4px;vertical-align:0}
.mains .item{line-height:1.68}
.teppan .item{font-size:7.4px;line-height:1.88}
.teppan .item .price{font-size:8.8px}
.fine-print{font-size:5.6px;text-align:center;line-height:1.3;margin-top:3px}
.leaf-art{position:absolute;background:linear-gradient(135deg,rgba(184,137,31,.22),rgba(184,137,31,.08));border-radius:40% 10% 40% 10%}
.leaf-side{right:-6px;top:330px;width:40px;height:70px}
.leaf-bottom{left:50%;transform:translateX(-50%);bottom:10px;width:105px;height:62px;border-radius:50% 50% 40% 40%}
.corner{position:absolute;width:9px;height:9px;border:1px solid var(--gold)}
.c-tl{top:2px;left:2px}.c-tr{top:2px;right:2px}.c-bl{bottom:2px;left:2px}.c-br{bottom:2px;right:2px}
</style>
</head>
<body>

<article class="menu-card" aria-label="Lunch Specials menu">
  <div class="menu-frame">
    <span class="corner c-tl"></span><span class="corner c-tr"></span><span class="corner c-bl"></span><span class="corner c-br"></span>
    <h1 class="menu-title">Lunch Specials</h1>
    <p class="menu-hours">(Served Daily 11 am - 3 pm)</p>
    <div class="divider"><span></span></div>

    <section class="sandwiches">
      <h2 class="section-title">Sandwiches</h2>
      <p class="section-note">Served with Choice of Miso Soup or House<br>Salad &amp; Potato Chips</p>
      <ul class="item-list">
        <li class="item"><span>Fried Breaded Calamari Steak<span class="item-desc">with Tomato, Lettuce &amp; Onion</span></span><span class="price">$16</span></li>
        <li class="item"><span>Grilled Chicken<span class="item-desc">with Bacon, Tomato, Lettuce &amp; Mayonnaise Drizzle</span></span><span class="price">$16</span></li>
        <li class="item"><span>Hamburger<span class="item-desc">with Lettuce, Tomato, Onion, Mayonnaise Drizzle</span></span><span class="price">$18</span></li>
        <li class="item"><span>Fried Soft Shell Crab Burger<span class="item-desc">with Avocado, Lettuce, Tomato, Onion &amp; Mayo</span></span><span class="price">$20</span></li>
      </ul>
    </section>
    <div class="divider"><span></span></div>

    <section class="sushi">
      <h2 class="section-title">Sushi Specials</h2>
      <p class="section-note">Please Select 4 of the followings for $ 16</p>
      <p class="section-note">Served with a 4 piece California Roll &amp;<br>Miso Soup or House Salad</p>
      <ul class="sushi-grid">
        <li>Hamachi <span class="inline-desc">- Yellowtail Tuna</span></li>
        <li>Maguro <span class="inline-desc">- Yellow fin Tuna</span></li>
        <li>Hotate <span class="inline-desc">- Scallop</span></li>
        <li>Smoked Salmon</li>
        <li>Ika <span class="inline-desc">- Squid</span></li>
        <li>Tako <span class="inline-desc">- Octopus</span></li>
        <li>Ikura <span class="inline-desc">- Salmon Roe</span></li>
        <li>Unagi <span class="inline-desc">- BBQ Eel</span></li>
        <li>Saba <span class="inline-desc">- Mackerel</span></li>
        <li>Ebi <span class="inline-desc">- Shrimp</span></li>
        <li>Sake <span class="inline-desc">- Salmon</span></li>
        <li>Tamago <span class="inline-desc">- Egg</span></li>
        <li>Tai <span class="inline-desc">- Red Snapper</span></li>
      </ul>
    </section>
    <div class="divider"><span></span></div>

    <section class="mains">
      <h2 class="section-title">Main Courses</h2>
      <p class="section-note">Served with Rice &amp; Choice of Miso Soup<br>or House Salad</p>
      <p class="section-note">All Meals Served with Rice.<br>Upgrade to fried rice for only $4</p>
      <ul class="item-list">
        <li class="item"><span>Organic Tofu Teriyaki <span class="inline-desc">- Served Grilled or Tempura Fried</span></span><span class="price">$14</span></li>
        <li class="item"><span>Chicken Teriyaki</span><span class="price">$16</span></li>
        <li class="item"><span>Spicy Chicken Teriyaki</span><span class="price">$16</span></li>
        <li class="item"><span>Beef Teriyaki</span><span class="price">$16</span></li>
        <li class="item"><span>Spicy Beef Teriyaki</span><span class="price">$16</span></li>
        <li class="item"><span>Chicken Katsu <span class="inline-desc">-Breaded Chicken Breast</span></span><span class="price">$15</span></li>
        <li class="item"><span>Katsu Don <span class="inline-desc">- Fried Chicken Breast, Egg &amp; Onion over Rice</span></span><span class="price">$16</span></li>
        <li class="item"><span>Unagi Don <span class="inline-desc">- BBQ Eel over Rice</span></span><span class="price">$19</span></li>
        <li class="item"><span>Shrimp &amp; Vegetable Tempura</span><span class="price">$16</span></li>
      </ul>
    </section>
    <div class="divider"><span></span></div>

    <section class="notice">
      <h2 class="section-title">Served Raw</h2>
      <p class="fine-print">20% gratuity added to parties of 6 or more.<br>Consuming raw or undercooked food may increase<br>your risk of foodborne illness</p>
    </section>
    <div class="leaf-art leaf-side" role="img" aria-label="Gold line-drawn leaf sprig decoration"></div>
  </div>
</article>

<article class="menu-card" aria-label="Teppanyaki Lunch menu">
  <div class="menu-frame">
    <span class="corner c-tl"></span><span class="corner c-tr"></span><span class="corner c-bl"></span><span class="corner c-br"></span>
    <h1 class="menu-title">Teppanyaki Lunch</h1>
    <p class="menu-hours">(Available until 11 am-2:30 pm)</p>
    <div class="divider"><span></span></div>

    <section class="teppan">
      <p class="section-note gold">Served with Miso Soup or Salad, Choice of<br>Rice &amp; Vegetables</p>
      <ul class="item-list">
        <li class="item"><span>Hibachi Chicken</span><span class="price">$18.00</span></li>
        <li class="item"><span>Hibachi Shrimp</span><span class="price">$19.00</span></li>
        <li class="item"><span>Hibachi New York Steak</span><span class="price">$20.00</span></li>
        <li class="item"><span>Hibachi Salmon</span><span class="price">$20.00</span></li>
        <li class="item"><span>Teriyaki Beef</span><span class="price">$19.00</span></li>
        <li class="item"><span>Hibachi Scallop</span><span class="price">$20.00</span></li>
        <li class="item"><span>Chicken and Shrimp</span><span class="price">$21.00</span></li>
        <li class="item"><span>Scallop and Shrimp</span><span class="price">$22.00</span></li>
        <li class="item"><span>New York Steak and Chicken</span><span class="price">$22.00</span></li>
        <li class="item"><span>New York Steak and Shrimp</span><span class="price">$23.00</span></li>
        <li class="item"><span>New York Steak and Scallop</span><span class="price">$24.00</span></li>
        <li class="item"><span>Filet Mignon</span><span class="price">$23.00</span></li>
        <li class="item"><span>Filet Mignon and Chicken</span><span class="price">$25.00</span></li>
        <li class="item"><span>Filet Mignon and Shrimp</span><span class="price">$26.00</span></li>
        <li class="item"><span>Filet Mignon and Scallop</span><span class="price">$27.00</span></li>
      </ul>
    </section>
    <div class="divider" style="margin-top:10px"><span></span></div>

    <section class="teppan">
      <h2 class="menu-title" style="margin-top:10px">Special Menu</h2>
      <p class="menu-hours" style="margin-top:4px">(Ages 12 and Under ~ Ages 65 and Older)</p>
      <div class="divider"><span></span></div>
      <p class="section-note gold">Served with Miso Soup or Salad, Choice of<br>Rice &amp; Vegetables</p>
      <ul class="item-list">
        <li class="item"><span>Hibachi Chicken</span><span class="price">$15.00</span></li>
        <li class="item"><span>Hibachi Shrimp</span><span class="price">$16.00</span></li>
        <li class="item"><span>Hibachi Scallop</span><span class="price">$18.00</span></li>
        <li class="item"><span>Hibachi New York Steak</span><span class="price">$18.00</span></li>
        <li class="item"><span>Hibachi Scallop</span><span class="price">$18.00</span></li>
        <li class="item"><span>Teriyaki Beef</span><span class="price">$16.00</span></li>
      </ul>
      <div class="divider" style="margin-top:8px"><span></span></div>
    </section>
    <div class="leaf-art leaf-bottom" role="img" aria-label="Gold line-drawn leaves and blossom decoration"></div>
  </div>
</article>

</body>
</html>
```